Solar energy proposal for homeowners

I am providing households with solar energy proposals, and I need a high-quality brochure that is packaged cleverly to attract the homeowner's attention. Take a look at the one page solar brochure that I have included to get an idea of text and content.

Target Market(s)

Residential Homeowners

Industry/Entity Type

Solar

Requirements
Must have
• High quality document

```html
<!DOCTYPE html>
<html lang="en">
<head>
<meta charset="utf-8">
<title>Brightvale Energy – Solar for $0 Down</title>
<link rel="stylesheet" href="https://fonts.googleapis.com/css2?family=Figtree:wght@600;700;800&family=Kumbh+Sans:wght@400;600&family=Poppins:wght@500;600;700&display=swap">
<style>
  :root {
    --navy: #3a4572;
    --teal: #22b5c8;
    --lime: #a3d68f;
    --ink: #3b3f4e;
    --white: #ffffff;
    --sky-top: #6c8fc4;
    --sky-bottom: #93b2d8;
    --brand-gradient: linear-gradient(90deg, var(--teal) 0%, var(--lime) 100%);
  }
  * { box-sizing: border-box; margin: 0; padding: 0; }
  html, body { width: 927px; height: 1200px; overflow: hidden; background: var(--navy); }
  .flyer {
    position: relative;
    width: 927px;
    height: 1200px;
    background: var(--navy);
    color: var(--white);
    font-family: "Kumbh Sans", sans-serif;
    overflow: hidden;
  }

  /* Brand */
  .brand {
    position: absolute;
    z-index: 2;
    left: 74px; top: 66px;
    display: flex; align-items: center; gap: 10px;
    white-space: nowrap;
  }
  .brand-dot {
    width: 28px; height: 28px; border-radius: 50%;
    background: var(--teal);
    flex: none;
  }
  .brand-name {
    font-family: "Kumbh Sans", sans-serif;
    font-weight: 400;
    font-size: 30px;
    color: var(--teal);
    line-height: 1;
  }

  /* Hero photo area */
  .hero-photo {
    position: absolute;
    left: 432px; top: 0;
    width: 495px; height: 452px;
    background: linear-gradient(180deg, var(--sky-top) 0%, var(--sky-bottom) 100%);
  }

  /* Headline panel */
  .headline-panel {
    position: absolute;
    left: 4px; top: 151px;
    width: 456px; height: 344px;
    background: var(--brand-gradient);
  }
  .headline {
    position: absolute;
    left: 47px; top: 14px;
    font-family: "Figtree", sans-serif;
    font-weight: 800;
    font-size: 54px;
    line-height: 65px;
    letter-spacing: -0.5px;
    color: var(--white);
  }
  .headline-sub {
    position: absolute;
    left: 50px; top: 275px;
    font-size: 21px;
    line-height: 26px;
    color: var(--ink);
  }

  /* Section headings */
  .section-title {
    position: absolute;
    font-family: "Figtree", sans-serif;
    font-weight: 700;
    font-size: 37px;
    line-height: 1;
    color: var(--white);
  }

  /* Why choose us */
  .why-title { left: 22px; top: 530px; }
  .benefits {
    position: absolute;
    left: 24px; top: 578px;
    list-style: none;
    font-size: 21px;
    line-height: 25.5px;
  }
  .benefits li::before {
    content: "";
    display: inline-block;
    width: 5px; height: 5px; border-radius: 50%;
    background: var(--white);
    margin: 0 11px 4px 0;
    vertical-align: middle;
  }

  /* About */
  .about-title { left: 502px; top: 489px; }
  .about-text {
    position: absolute;
    left: 503px; top: 536px;
    font-size: 17.5px;
    line-height: 21.8px;
    letter-spacing: 0.35px;
    white-space: nowrap;
  }
  .about-text strong { font-weight: 600; font-size: 20px; letter-spacing: 0; }

  /* Services */
  .service-title-main { left: 22px; top: 757px; }
  .service {
    position: absolute;
    white-space: nowrap;
  }
  .service-icon {
    position: absolute;
    left: -76px; top: 17px;
    width: 44px; height: 39px;
  }
  .service h3 {
    font-family: "Figtree", sans-serif;
    font-weight: 600;
    font-size: 23px;
    line-height: 28px;
    margin-bottom: 3px;
  }
  .service p {
    font-size: 17.5px;
    line-height: 20.3px;
    letter-spacing: 0.35px;
  }
  .service p strong { font-weight: 600; }
  .svc-affordable { left: 98px; top: 808px; }
  .svc-installation { left: 98px; top: 915px; }
  .svc-installation p { line-height: 22.8px; margin-top: 6px; }
  .svc-local { left: 579px; top: 808px; }
  .svc-local p { line-height: 22.5px; margin-top: 2px; }
  .svc-eco { left: 580px; top: 914px; }
  .svc-eco p { line-height: 22px; margin-top: 3px; }

  /* Footer call to action */
  .cta {
    position: absolute;
    left: 0; top: 1056px;
    width: 927px; height: 144px;
    background: var(--brand-gradient);
    color: var(--ink);
    font-family: "Poppins", sans-serif;
    text-align: center;
  }
  .cta-title {
    margin-top: 13px;
    font-weight: 700;
    font-size: 35px;
    line-height: 44px;
  }
  .cta-tagline {
    margin-top: 2px;
    font-weight: 500;
    font-size: 20px;
    line-height: 26px;
  }
  .cta-contacts {
    display: flex;
    justify-content: center;
    gap: 52px;
    margin-top: 18px;
    font-weight: 600;
    font-size: 18px;
    line-height: 22px;
  }
</style>
</head>
<body>
<main class="flyer">

  <div class="hero-photo" role="img" aria-label="Photo of a house with rooftop solar panels and a garden under a clear blue sky"></div>

  <div class="brand">
    <span class="brand-dot"></span>
    <span class="brand-name">Brightvale Energy</span>
  </div>

  <section class="headline-panel">
    <h1 class="headline">SOLAR FOR<br>$0 DOWN.<br>NO LIENS.<br>NO KIDDING.</h1>
    <p class="headline-sub">Power Your Future with<br>Brightvale Energy</p>
  </section>

  <h2 class="section-title why-title">Why Choose Us?</h2>
  <ul class="benefits">
    <li>No financing</li>
    <li>No liens</li>
    <li>No down payment</li>
    <li>No insurance costs</li>
    <li>No long-term commitment</li>
    <li>No maintenance costs</li>
  </ul>

  <h2 class="section-title about-title">About Us</h2>
  <p class="about-text"><strong>At Brightvale Energy,</strong> we make going solar<br>simple, affordable, and stress-free for<br>homeowners. Our approach is built on<br>transparency—no pushy sales, no complicated<br>contracts, and no hidden costs. We provide<br>clear information and smart solutions that help<br>you confidently switch to clean energy while<br>lowering your monthly electricity bills.</p>

  <h2 class="section-title service-title-main">Our Best Service</h2>

  <svg width="0" height="0" style="position:absolute">
    <defs>
      <linearGradient id="hexFill" x1="0" y1="0" x2="1" y2="0">
        <stop offset="0" stop-color="#22b5c8"/>
        <stop offset="1" stop-color="#a3d68f"/>
      </linearGradient>
      <symbol id="hex" viewBox="0 0 44 39">
        <polygon points="11,0 33,0 44,19.5 33,39 11,39 0,19.5" fill="url(#hexFill)"/>
      </symbol>
    </defs>
  </svg>

  <article class="service svc-affordable">
    <svg class="service-icon" aria-hidden="true"><use href="#hex"/></svg>
    <h3>Affordable &amp; Transparent</h3>
    <p><strong>Simple pricing</strong> with no hidden fees.<br>Enjoy a fixed monthly rate that’s lower<br>than typical electricity bills.</p>
  </article>

  <article class="service svc-installation">
    <svg class="service-icon" aria-hidden="true"><use href="#hex"/></svg>
    <h3>Expert Installation</h3>
    <p>Certified professionals handle everything<br>—from installation to maintenance and<br>support—so you don’t have to worry.</p>
  </article>

  <article class="service svc-local">
    <svg class="service-icon" aria-hidden="true"><use href="#hex"/></svg>
    <h3>Local Expertise</h3>
    <p>Our local team understands the needs<br>of homeowners and delivers solutions<br>tailored to your area and utility rates.</p>
  </article>

  <article class="service svc-eco">
    <svg class="service-icon" aria-hidden="true"><use href="#hex"/></svg>
    <h3>Eco-Friendly</h3>
    <p>Switch to clean, renewable solar<br>energy and reduce your carbon<br>footprint while powering your home<br>responsibly.</p>
  </article>

  <footer class="cta">
    <h2 class="cta-title">Get Your Free Solar Proposal</h2>
    <p class="cta-tagline">No obligation. No pressure. Just honest solar solutions.</p>
    <div class="cta-contacts">
      <span class="cta-phone">(555)214-3870</span>
      <span class="cta-address">48 Meadow Lane, Fairview</span>
      <span class="cta-web">www.brightvaleenergy.com</span>
    </div>
  </footer>

</main>
</body>
</html>
```